Past The Hedge landscaping flyer "looking for BIG impact"

We're doing a big marketing push and having 50,000 flyers distributed around exeter, devon.

A5

The flyer is double sided but withe the same image on each side so it doesn't matter how it lands.

Flyer for landscape gardener and maintenance company.

Solo drop leaflets so really needs to pop.

Would like it to be similar to website

4 elements of flyer are:

Design
Past The Hedge Garden Design offers a full-service garden design consultancy to clients seeking an outside space which is both beautiful and functional, any size, any budget.

Create
We provide high quality, bespoke garden construction for homes and businesses throughout Devon and the South West.

Maintain
Services include grass mowing, hedge trimming and cutting, pruning, weeding, pressure cleaning and lawn care, planting and turfing.

Contact details
Office 01392 417253
Mobile 07914362587
Rcarver@pastthehedgeltd.example
Www.pastthehedgeltd.example

Images and company logo attached.

I've added something I have very crudely mocked up. Use it or ignore it, I really don't mind.

I've added two pics for maintenance, one is a few hand tools and one is a mower. Up to you which one you choose.

Cheers!

Reason: Deadline extended. We aren't so rushed now so we're taking the pressure off. Really impressed with what we've received so far!

Requirements
Must have
• BIG IMPACT.
• EYE CATCHING
• SHOWS WHAT WE DO.
• Maintain brand recognition.

```html
<!DOCTYPE html>
<html lang="en">
<head>
<meta charset="utf-8">
<title>Past The Hedge – Flyer</title>
<link rel="stylesheet" href="https://fonts.googleapis.com/css2?family=Open+Sans:wght@400;600&display=swap">
<style>
  :root {
    --page-bg: #e9e6e1;
    --sky-top: #c4f1f7;
    --sky-bottom: #f4fcfd;
    --grass-light: #9be05a;
    --grass-deep: #4fae22;
    --shard-bright: #45dc14;
    --shard-mid: #2fc00c;
    --globe: #3bc21a;
    --globe-rim: #1f4a1a;
    --panel: rgba(24, 26, 25, 0.94);
    --panel-photo: #262a27;
    --accent: #4ee62a;
    --text-light: #ffffff;
    --divider: rgba(255, 255, 255, 0.18);
  }
  * { box-sizing: border-box; margin: 0; padding: 0; }
  html, body {
    width: 1200px; height: 1000px; overflow: hidden;
    background: var(--page-bg);
    font-family: "Open Sans", Arial, sans-serif;
  }
  .flyer {
    position: absolute; left: 24px; top: 95px;
    width: 1148px; height: 810px; overflow: hidden;
    background: linear-gradient(180deg, var(--sky-top) 0%, var(--sky-bottom) 70%);
    box-shadow: 0 2px 10px rgba(0,0,0,0.18);
  }
  .grass {
    position: absolute; left: 0; right: 0; bottom: 0; height: 470px;
    background:
      radial-gradient(ellipse 420px 330px at 1060px 400px, var(--grass-light) 0%, rgba(155,224,90,0.55) 45%, rgba(155,224,90,0) 75%),
      linear-gradient(180deg, rgba(155,224,90,0) 55%, rgba(155,224,90,0.7) 78%, var(--grass-deep) 100%);
  }
  .haze-panel {
    position: absolute; left: 31px; top: 23px; width: 383px; height: 182px;
    background: rgba(255,255,255,0.35);
  }
  .shards { position: absolute; inset: 0; }
  .service {
    position: absolute; width: 290px; height: 200px;
    color: var(--text-light); text-align: center;
    box-shadow: 0 4px 10px rgba(0,0,0,0.25);
  }
  .service__photo {
    position: absolute; inset: 0;
    background: linear-gradient(180deg, var(--panel-photo), #141615);
  }
  .service__body { position: absolute; inset: 0; background: var(--panel); padding: 0 18px; }
  .service--design { left: 160px; top: 78px; }
  .service--create { left: 719px; top: 78px; }
  .service--maintain { left: 152px; top: 520px; }
  .service--contact { left: 719px; top: 520px; height: 198px; }
  .service__icon { display: block; margin: 16px auto 0; width: 50px; height: 50px; }
  .service__title {
    font-weight: 400; font-size: 17px; letter-spacing: 0.5px;
    text-transform: uppercase; margin-top: 10px;
  }
  .service__text { font-size: 11px; line-height: 14px; margin-top: 14px; }
  .service--design .service__text { text-align: justify; text-align-last: center; }
  .contact__heading {
    color: var(--accent); font-size: 16px; line-height: 23px;
    font-weight: 400; margin-top: 8px; text-transform: uppercase;
  }
  .contact__list { list-style: none; margin: 24px auto 0; width: 180px; font-size: 11.5px; }
  .contact__list li { line-height: 22px; border-bottom: 1px solid var(--divider); }
  .contact__list li:last-child { border-bottom: none; }
  .brand {
    position: absolute; left: 497px; top: 338px; width: 170px; height: 170px;
    border-radius: 50%; background: var(--globe);
    border: 4px solid var(--globe-rim);
    display: flex; align-items: center; justify-content: center; text-align: center;
  }
  .brand__name {
    color: var(--text-light); font-weight: 600; font-size: 20px;
    line-height: 24px; text-transform: uppercase; width: 130px;
  }
</style>
</head>
<body>
<main class="flyer">
  <div class="grass" role="img" aria-label="Photograph of tall green grass under a clear sky"></div>
  <div class="haze-panel"></div>

  <svg class="shards" width="1148" height="810" viewBox="0 0 1148 810" aria-hidden="true">
    <polygon points="450,78 450,278 520,350" fill="var(--shard-bright)"/>
    <polygon points="160,278 450,278 520,350" fill="var(--shard-mid)"/>
    <polygon points="719,78 719,278 644,350" fill="var(--shard-bright)"/>
    <polygon points="719,278 1009,278 644,350" fill="var(--shard-mid)"/>
    <polygon points="152,520 442,520 515,480" fill="var(--shard-mid)"/>
    <polygon points="442,520 442,720 515,480" fill="var(--shard-bright)"/>
    <polygon points="719,520 1009,520 650,480" fill="var(--shard-mid)"/>
    <polygon points="719,520 719,718 650,480" fill="var(--shard-bright)"/>
  </svg>

  <section class="service service--design">
    <div class="service__photo" role="img" aria-label="Faint garden plan drawing"></div>
    <div class="service__body">
      <svg class="service__icon" viewBox="0 0 50 50" aria-hidden="true">
        <path d="M30 12 H8 V44 H40 V26" fill="none" stroke="#fff" stroke-width="4"/>
        <path d="M44 4 C30 8 22 20 20 34 L24 34 C30 28 38 20 44 4 Z" fill="#fff"/>
      </svg>
      <h2 class="service__title">Design</h2>
      <p class="service__text">Past The Hedge Garden Design offers a full-service garden design consultancy to clients seeking an outside space which is both beautiful and functional, any size, any budget.</p>
    </div>
  </section>

  <section class="service service--create">
    <div class="service__photo" role="img" aria-label="Faint photograph of a house and garden path"></div>
    <div class="service__body">
      <svg class="service__icon" viewBox="0 0 50 50" aria-hidden="true">
        <path d="M36 6 L46 16 L20 42 L8 46 L12 34 Z" fill="#fff"/>
        <path d="M12 34 L20 42" stroke="#1b1d1c" stroke-width="2"/>
      </svg>
      <h2 class="service__title">Create</h2>
      <p class="service__text">We provide high quality, bespoke garden construction for homes and businesses throughout Devon and the South West.</p>
    </div>
  </section>

  <section class="service service--maintain">
    <div class="service__photo" role="img" aria-label="Faint photograph of a lawn mower on grass"></div>
    <div class="service__body">
      <svg class="service__icon" viewBox="0 0 50 50" aria-hidden="true">
        <g fill="none" stroke="#fff" stroke-width="3.5">
          <ellipse cx="25" cy="25" rx="21" ry="8"/>
          <ellipse cx="25" cy="25" rx="21" ry="8" transform="rotate(60 25 25)"/>
          <ellipse cx="25" cy="25" rx="21" ry="8" transform="rotate(-60 25 25)"/>
        </g>
      </svg>
      <h2 class="service__title">Maintain</h2>
      <p class="service__text">Services include grass mowing, hedge trimming and cutting, pruning, weeding, pressure cleaning and lawn care, planting and turfing.</p>
    </div>
  </section>

  <section class="service service--contact">
    <div class="service__body">
      <h2 class="contact__heading">Contact us now<br>for a free quotation</h2>
      <ul class="contact__list">
        <li>Office 01392 417253</li>
        <li>Mobile 07914362587</li>
        <li>Rcarver@pastthehedgeltd.example</li>
        <li>www.pastthehedgeltd.example</li>
      </ul>
    </div>
  </section>

  <div class="brand">
    <span class="brand__name">Past The Hedge</span>
  </div>
</main>
</body>
</html>
```